Bus Bench Ad Design Needed

Hi there. We would like to design an eye catching bus bench ad! The information that we would like to have on it is found below:

- Our logo which is attached below. We would this to take up at least half of the bus bench.
- Our phone number in bold, very visible to see. 813-562-0947. White numbers on an eye catching colored background.
- Our web address : www.SplitEase247.example
- A "Ring Gary" phrase in a black circle with yellow bold letters. Want the "Ring Gary" to be somewhat angled. We are thinking that the "Ring Gary" should be directly below the image in our logo.
- Our tag line we want somewhere in here as well which is "Divorce made easy - at a price you'll like!"

```html
<!DOCTYPE html>
<html lang="en">
<head>
<meta charset="UTF-8">
<title>SplitEase Bench Ad</title>
<link rel="stylesheet" href="https://fonts.googleapis.com/css2?family=League+Spartan:wght@600;700&family=Marcellus&family=Didact+Gothic&display=swap">
<style>
  :root {
    --page: #e6e6e6;
    --white: #ffffff;
    --brand-blue: #1a84c7;
    --ink: #1a1a1a;
    --call-yellow: #fff200;
    --black: #000000;
  }
  html, body {
    margin: 0;
    padding: 0;
    width: 1200px;
    height: 960px;
    overflow: hidden;
    background: var(--page);
  }
  .bench-ad {
    position: absolute;
    left: 40px;
    top: 331px;
    width: 1120px;
    height: 297px;
    background: var(--white);
    overflow: hidden;
  }
  .brand {
    position: absolute;
    top: 0;
    left: 0;
    width: 100%;
    height: 162px;
  }
  .brand-mark {
    position: absolute;
    left: 230px;
    top: 42px;
    width: 72px;
    height: 72px;
    background: var(--brand-blue);
  }
  .brand-divider {
    position: absolute;
    left: 348px;
    top: 38px;
    width: 2px;
    height: 104px;
    background: #c9c9c9;
  }
  .brand-name {
    position: absolute;
    left: 362px;
    top: 22px;
    margin: 0;
    font-family: "Marcellus", serif;
    font-weight: 400;
    font-size: 82px;
    line-height: 1;
    letter-spacing: 3px;
    color: var(--brand-blue);
  }
  .brand-service {
    position: absolute;
    left: 364px;
    top: 108px;
    margin: 0;
    font-family: "Didact Gothic", sans-serif;
    font-size: 34px;
    line-height: 1;
    color: var(--ink);
  }
  .contact-band {
    position: absolute;
    left: 0;
    top: 162px;
    width: 100%;
    height: 135px;
    background: var(--brand-blue);
  }
  .tagline {
    position: absolute;
    left: 15px;
    top: 28px;
    margin: 0;
    font-family: "League Spartan", sans-serif;
    font-weight: 700;
    font-size: 37px;
    line-height: 1.15;
    color: var(--white);
  }
  .call-badge {
    position: absolute;
    left: 401px;
    top: 139px;
    width: 176px;
    height: 176px;
    border-radius: 50%;
    background: var(--white);
  }
  .call-badge-inner {
    position: absolute;
    left: 15px;
    top: 14px;
    width: 146px;
    height: 146px;
    border-radius: 50%;
    background: var(--black);
    display: flex;
    flex-direction: column;
    align-items: center;
    justify-content: center;
    font-family: "League Spartan", sans-serif;
    font-weight: 700;
    font-size: 38px;
    line-height: 1;
    color: var(--call-yellow);
    text-align: center;
  }
  .call-badge-inner span { display: block; padding-top: 4px; }
  .phone {
    position: absolute;
    right: 24px;
    top: 14px;
    margin: 0;
    font-family: "League Spartan", sans-serif;
    font-weight: 700;
    font-size: 70px;
    line-height: 1;
    color: var(--white);
  }
  .website {
    position: absolute;
    right: 26px;
    top: 88px;
    margin: 0;
    font-family: "League Spartan", sans-serif;
    font-weight: 700;
    font-size: 29px;
    line-height: 1;
    color: var(--ink);
  }
</style>
</head>
<body>
  <section class="bench-ad">
    <header class="brand">
      <div class="brand-mark"></div>
      <div class="brand-divider"></div>
      <h1 class="brand-name">SplitEase</h1>
      <p class="brand-service">Non-Lawyer Documents Service</p>
    </header>
    <div class="contact-band">
      <p class="tagline">Divorce made easy<br>at a price you'll like!</p>
      <p class="phone">813-562-0947</p>
      <p class="website">www.SplitEase247.example</p>
    </div>
    <div class="call-badge">
      <div class="call-badge-inner"><span>RING</span><span>GARY</span></div>
    </div>
  </section>
</body>
</html>
```